TKN Music Studios

I need a website for two locations, description of services, possible merchandise page, PDFs of faculty, bios, live performance of both faculty and students, testimonial page, pre-college prep page for musical theatre, links to our social media, link to our registration page, link to affiliate programming resources

```html
<!DOCTYPE html>
<html lang="en">
<head>
<meta charset="utf-8">
<title>TKN Music Studios</title>
<link rel="stylesheet" href="https://fonts.googleapis.com/css2?family=Tinos:wght@400;700&family=PT+Sans:wght@400;700&family=Arimo:wght@400;700&display=swap">
<style>
:root{
  --peach:#f5c296;
  --peach-deep:#f0b585;
  --frame-line:#e08a6a;
  --purple:#6a4a8c;
  --bar-top:#b9cbd2;
  --bar-bottom:#9fb2ba;
  --bar-shadow:#6e7f86;
  --olive:#c5c878;
  --olive-dark:#a9ac5c;
  --olive-text:#a3a64e;
  --link-brown:#9a7a3a;
  --coral:#e0805a;
  --white:#ffffff;
}
*{box-sizing:border-box;margin:0;padding:0}
html,body{width:1200px;height:1021px;overflow:hidden}
body{position:relative;background:var(--peach);font-family:"PT Sans",sans-serif;color:var(--purple)}
.backdrop{position:absolute;inset:0;background:radial-gradient(circle at 50% 50%,var(--peach) 0%,var(--peach-deep) 100%)}
.frame{position:absolute;left:0;top:0;width:1200px;height:1021px}
.site-title{position:absolute;left:0;width:1200px;top:97px;text-align:center;font-family:"Tinos",serif;font-size:29.5px;font-weight:400;color:var(--purple)}
.bar{position:absolute;left:188px;width:825px;height:36px;background:linear-gradient(var(--bar-top),var(--bar-bottom))}
.bar::before,.bar::after{content:"";position:absolute;bottom:-8px;border-top:8px solid var(--bar-shadow)}
.bar::before{left:0;border-left:12px solid transparent}
.bar::after{right:0;border-right:12px solid transparent}
.main-nav{top:146px;display:flex}
.main-nav a{display:block;height:36px;line-height:36px;padding:0 19px 0 20px;color:var(--white);font-size:12px;font-weight:700;text-decoration:none;text-shadow:0 1px 1px rgba(0,0,0,.35);border-right:1px dotted rgba(255,255,255,.7)}
.intro{position:absolute;left:240px;width:500px;text-align:center}
.welcome{top:198px;font-size:20px;font-weight:400;line-height:20px;color:var(--purple)}
.mission{top:289px;font-family:"Tinos",serif;font-size:12px;line-height:18.5px;color:var(--purple)}
.mission .lead{font-family:"PT Sans",sans-serif;font-size:13px}
.offer{font-family:"Arimo",sans-serif;font-weight:700;font-size:11.7px;line-height:17.4px;color:var(--purple)}
.offer-phx{top:383px}
.offer-fl{top:538px}
.offer-career{top:659px}
.login-box{position:absolute;left:757px;top:214px;width:253px;height:244px;border:4px solid var(--olive);background:var(--white);padding:8px 11px}
.login-box::after{content:"";position:absolute;right:-4px;bottom:-12px;border-top:8px solid var(--olive-dark);border-right:9px solid transparent}
.login-box h2{font-size:11px;font-weight:700;color:var(--olive-text);padding-bottom:6px;border-bottom:1px dotted #ccc}
.login-box p{font-size:9.5px;color:var(--purple);margin-top:9px}
.field{margin-top:16px}
.field label{display:block;font-size:8.8px;color:var(--purple);margin-bottom:3px}
.field .input{position:relative;height:25px;border:1px solid #d8d8d8}
.field .input::after{content:"";position:absolute;right:7px;top:6px;width:12px;height:11px;border-radius:2px;background:#777}
.field+.field{margin-top:10px}
.remember{display:flex;align-items:center;gap:9px;font-size:8.8px;margin-top:10px}
.remember .box{width:9px;height:9px;border:1px solid #aaa;border-radius:2px}
.actions{margin-top:14px;font-size:8.8px;display:flex;align-items:center;gap:5px}
.actions .btn{border:1px solid #aaa;border-radius:3px;padding:1px 10px;color:#444;background:#f7f7f7}
.actions a{color:var(--link-brown);text-decoration:none}
.site-footer{top:858px;text-align:center;line-height:36px;font-size:9.5px;font-weight:700;color:var(--purple);text-shadow:0 1px 0 rgba(255,255,255,.3)}
.to-top{position:absolute;left:0;width:1200px;top:912px;display:flex;justify-content:center;align-items:center;gap:5px;font-size:9.8px;color:var(--coral)}
.to-top .icon{width:13px;height:13px;background:var(--olive);border-radius:2px;display:flex;align-items:center;justify-content:center}
</style>
</head>
<body>
<div class="backdrop" role="img" aria-label="Peach damask swirl wallpaper pattern"></div>

<svg class="frame" viewBox="0 0 1200 1021" aria-hidden="true">
  <path fill="#fff" d="M200,130 Q200,53 277,53 L540,53 Q590,42 600,0 Q610,42 660,53 L923,53 Q1000,53 1000,130 L1000,890 Q1000,967 923,967 L660,967 Q610,978 600,1021 Q590,978 540,967 L277,967 Q200,967 200,890 Z"/>
  <path fill="none" stroke="#e08a6a" stroke-width="2" d="M224,150 Q224,77 297,77 L545,77 Q585,70 600,40 Q615,70 655,77 L903,77 Q976,77 976,150 L976,870 Q976,944 903,944 L655,944 Q615,951 600,981 Q585,951 545,944 L297,944 Q224,944 224,870 Z"/>
</svg>

<h1 class="site-title">TKN MUSIC STUDIOS</h1>

<nav class="bar main-nav">
  <a href="#">HOME</a>
  <a href="#">FLORIDA FACULTY</a>
  <a href="#">PHOENIX FACULTY</a>
  <a href="#">LOGIN</a>
  <a href="#">PHOTOS</a>
</nav>

<h2 class="intro welcome">WELCOME TO TKN MUSIC STUDIOS!<br>CELEBRATING OUR 15TH YEAR IN BUSINESS!</h2>

<p class="intro mission"><span class="lead">A NATIONAL BOUTIQUE MUSIC AND CAREER CONSULTATION STUDIO WHERE<br>STUDENTS OF ALL AGES</span>&nbsp; LEARN TO DEVELOP THEIR OWN UNIQUE LOVE OF MUSIC<br>AND THE PHYSICAL AND MENTAL SKILL SETS TO BECOME A SUCCESSFUL STUDENT,<br>MUSICIAN, AND PERFORMER!</p>

<div class="intro offer offer-phx">
  We Specialize in the following instruments:<br>
  Phoenix Studio:<br>
  PIANO/VOICE<br>
  GUITAR/BASS/UKULELE<br>
  DRUMS<br>
  VIOLIN/FLUTE
</div>

<div class="intro offer offer-fl">
  South Florida Studio:<br>
  PIANO/VOICE<br>
  DRUMS/GUITAR/UKULELE<br>
  SAXOPHONE/CLARINET
</div>

<div class="intro offer offer-career">
  PHX/FLL:<br>
  Classical Career Management:College Preparatory Consultation for Sophmores,<br>Juniors, and Seniors(MT,BM-Voice)<br>
  Career Management:All ages welcome to develop talent for commercial, print, dance,<br>acting/movies, recording
</div>

<aside class="login-box">
  <h2>LOGIN</h2>
  <p>Login to your Lesson Desk Helper account.</p>
  <div class="field"><label>Username</label><div class="input"></div></div>
  <div class="field"><label>Password</label><div class="input"></div></div>
  <div class="remember"><span class="box"></span>Keep me logged in on this device</div>
  <div class="actions"><span class="btn">Login</span> or <a href="#">Reset password</a></div>
</aside>

<footer class="bar site-footer">COPYRIGHT © 2020 · POWERED BY LESSON DESK HELPER</footer>

<div class="to-top">
  <span class="icon"><svg width="9" height="6" viewBox="0 0 9 6"><path d="M1,5 L4.5,1.5 L8,5" fill="none" stroke="#fff" stroke-width="1.6"/></svg></span>
  RETURN TO TOP OF PAGE
</div>
</body>
</html>
```